Dental hygiene website

I would like to design to website that both dental professionals and the public can get information. I would also like a shopping cart as well. The name of the company is called Velqind. We have a product called the fresca one. Delia is the Ceo. Marcus is the CIO. Oliver is the COO. We are based in Parkland, Fl. The site should have a clean modern look that possibly has a natural/nature/ocean theme. We believe in an overall healthy lifestyle. We would like links to twitter/instagram/facebook. i would like to make additions to my shopping cart when we bring on new products. I would also like the ability to add new staff bio/photos when we add employees. The site must be able to be edited by myself once we take ownership.

sorry for the delay. I just uploaded the company logo

Reason: I forced to travel for business. please make any last minute submissions using the logo i uploaded. i will choose on october 25th

```html
<!DOCTYPE html>
<html lang="en">
<head>
<meta charset="UTF-8">
<title>Velqind Dental</title>
<link href="https://fonts.googleapis.com/css2?family=Montserrat:wght@400;500;600;700&display=swap" rel="stylesheet">
<style>
:root{
  --ocean-deep:#0b2f7a;
  --ocean-mid:#1a5fc0;
  --sky:#4fa3e0;
  --brand:#12a9e0;
  --ink:#1d1d1f;
  --text:#3a3a3a;
  --white:#ffffff;
}
*{box-sizing:border-box;margin:0;padding:0}
html,body{width:905px;height:1200px;overflow:hidden}
body{
  position:relative;
  font-family:'Montserrat',Arial,sans-serif;
  color:var(--text);
  background:linear-gradient(180deg,#3d8fd8 0%,#6fb3e6 26%,#f3e7c8 32%,#2a77cf 38%,#123f96 55%,var(--ocean-deep) 100%);
}
.header{position:absolute;left:130px;top:0;width:646px;height:68px}
.logo{position:absolute;font-weight:600;color:var(--brand);letter-spacing:-.3px;white-space:nowrap}
.header .logo{left:8px;top:23px;font-size:21px;color:var(--ink)}
.nav{position:absolute;top:31px;font-size:11px;color:var(--ink)}
.login{position:absolute;left:538px;top:26px;width:62px;height:24px;background:var(--brand);color:var(--white);font-size:9px;font-weight:700;display:flex;align-items:center;justify-content:center;gap:4px}
.cart{position:absolute;left:607px;top:26px;width:30px;height:24px;background:#4a4f57;display:flex;align-items:center;justify-content:center}
.hero{position:absolute;left:130px;top:68px;width:646px;height:250px;background:var(--white)}
.hero .logo{left:26px;top:53px;font-size:19px}
.hero-copy{position:absolute;left:28px;top:88px;width:245px;font-size:8.6px;line-height:13.6px;color:var(--text)}
.btn{position:absolute;background:var(--brand);color:var(--white);font-weight:700;display:flex;align-items:center;justify-content:center}
.hero .btn{left:26px;top:167px;width:154px;height:38px;font-size:11px}
.product-shot{position:absolute;left:345px;top:40px;width:278px;height:196px;background:radial-gradient(ellipse at 50% 50%,#dff1fb 0%,#ffffff 70%)}
.dots{position:absolute;left:288px;top:216px;display:flex;gap:8px;z-index:2}
.dot{width:11px;height:11px;border-radius:50%;background:var(--ink)}
.dot.active{background:var(--brand)}
.video-section{position:absolute;left:130px;top:318px;width:646px;height:373px;background:linear-gradient(180deg,rgba(255,240,210,.35) 0%,rgba(40,120,210,.25) 40%,rgba(30,110,210,.35) 100%)}
.section-label{position:absolute;left:0;width:646px;text-align:center;font-size:14px;color:var(--white);letter-spacing:-.2px;top:42px}
.video{position:absolute;left:64px;top:78px;width:516px;height:235px;background:var(--white);box-shadow:0 14px 18px -8px rgba(0,0,0,.55)}
.video .logo{left:38px;top:96px;font-size:19px}
.video-photo{position:absolute;left:142px;top:0;width:374px;height:235px;background:linear-gradient(90deg,#ffffff 0%,#f3e2d6 45%,#6b3b22 80%,#4a2815 100%)}
.play{position:absolute;left:219px;top:80px}
.featured{position:absolute;left:130px;top:691px;width:646px;height:400px;background:var(--white)}
.featured .section-label{color:var(--ink);top:24px;font-size:15px;font-weight:500}
.card{position:absolute;top:58px;width:180px;text-align:center}
.card-photo{width:170px;height:170px;margin:0 auto;border:3px solid var(--brand);border-radius:50%;background:radial-gradient(circle,#eaf6fc 0%,#ffffff 65%);box-shadow:0 6px 0 -2px #e4e4e4}
.card-title{margin-top:26px;font-size:12px;font-weight:500;color:var(--ink);line-height:13.5px}
.card-text{margin-top:10px;padding:0 12px;font-size:8.4px;line-height:13.6px;color:var(--text)}
.card .btn{position:relative;margin:19px auto 0;width:77px;height:25px;font-size:9px}
.footer{position:absolute;left:0;top:1091px;width:905px;text-align:center;color:var(--white)}
.social{display:flex;justify-content:center;gap:7px;margin-top:26px}
.social span{width:23px;height:23px;border-radius:50%;background:var(--white)}
.footer-links{margin-top:11px;font-size:9px}
.footer-links i{font-style:normal;margin:0 10px}
.copyright{margin-top:10px;font-size:8.5px}
</style>
</head>
<body>
<header class="header">
  <div class="logo">velqinddental</div>
  <span class="nav" style="left:280px">Home</span>
  <span class="nav" style="left:332px">About Us</span>
  <span class="nav" style="left:400px">Products</span>
  <span class="nav" style="left:464px">Contact Us</span>
  <div class="login">LOGIN
    <svg width="7" height="5" viewBox="0 0 7 5"><path d="M.5.5 3.5 3.8 6.5.5" stroke="#fff" stroke-width="1.4" fill="none"/></svg>
  </div>
  <div class="cart">
    <svg width="18" height="15" viewBox="0 0 18 15" fill="none" stroke="#fff" stroke-width="1.2"><path d="M1 1h3l2 9h9l2-7H5"/><circle cx="7" cy="13" r="1.2"/><circle cx="14" cy="13" r="1.2"/><path d="M6 5h10M7 7.5h8"/></svg>
  </div>
</header>

<section class="hero">
  <div class="logo">velqinddental</div>
  <p class="hero-copy">Lorem Ipsum is simply dummy text of the printing and typesetting industry. Lorem Ipsum has been the industry's standard dummy text ever since the 1500s, when an unknown printer took a galley of type and scrambled it to make a type specimen book.</p>
  <div class="btn">TRY FOR FREE DEMO</div>
  <div class="product-shot" role="img" aria-label="Photo of a white and blue electric toothbrush lying diagonally"></div>
  <div class="dots">
    <span class="dot active"></span><span class="dot"></span><span class="dot"></span><span class="dot"></span>
  </div>
</section>

<section class="video-section">
  <div class="section-label">INTRO VIDEO</div>
  <div class="video">
    <div class="video-photo" role="img" aria-label="Photo of a smiling woman brushing her teeth"></div>
    <div class="logo">velqinddental</div>
    <svg class="play" width="78" height="78" viewBox="0 0 78 78"><circle cx="39" cy="39" r="36" fill="none" stroke="#111" stroke-width="4"/><path d="M31 25 55 39 31 53Z" fill="#111"/></svg>
  </div>
</section>

<section class="featured">
  <div class="section-label">FEATURED PRODUCTS</div>
  <div class="card" style="left:30px">
    <div class="card-photo" role="img" aria-label="Photo of a white electric toothbrush with travel case"></div>
    <div class="card-title">Toothbrush<br>Product 1</div>
    <p class="card-text">Neque porro quisquam est qui dolorem ipsum quia dolor sit amet, consectetur, adipisci velit...</p>
    <div class="btn">ADD TO CART</div>
  </div>
  <div class="card" style="left:246px">
    <div class="card-photo" role="img" aria-label="Photo of a white and teal electric toothbrush on charger"></div>
    <div class="card-title">Toothbrush<br>Product2</div>
    <p class="card-text">Neque porro quisquam est qui dolorem ipsum quia dolor sit amet, consectetur, adipisci velit...</p>
    <div class="btn">ADD TO CART</div>
  </div>
  <div class="card" style="left:462px">
    <div class="card-photo" role="img" aria-label="Photo of a blue electric toothbrush on stand"></div>
    <div class="card-title">Toothbrush<br>Product 3</div>
    <p class="card-text">Neque porro quisquam est qui dolorem ipsum quia dolor sit amet, consectetur, adipisci velit...</p>
    <div class="btn">ADD TO CART</div>
  </div>
</section>

<footer class="footer">
  <div class="social">
    <span aria-label="Social link 1"></span>
    <span aria-label="Social link 2"></span>
    <span aria-label="Social link 3"></span>
  </div>
  <div class="footer-links">Home<i>|</i>About Us<i>|</i>Products<i>|</i>Services<i>|</i>FAQ's<i>|</i>Contact Us</div>
  <div class="copyright">© 2014 Company Name,al Rights Reserved</div>
</footer>
</body>
</html>
```